A billboard for Pine Hollow Construction size 36.5’ x 14.5’

Hi guys. We are purchasing a billboard and are looking for a design (size 36.5’ x 14.5’). Our slogan is "Quality you deserve, service you can count on". The goal of this billboard is brand recognition primarily letting people know we do roofs. Attached are logos that can be used if needed. Not necessarily all of them need to be used.

Target Market(s)

Residents in the local areas needing or thinking about a roof replacement

Industry/Entity Type

Roofing

Requirements
Must have
• Logo and services (roof replacement, gutters, siding, and snow removal)
Nice to have
• take a look at our website for ideas www.pinehollowconstruction.example

```html
<!DOCTYPE html>
<html lang="en">
<head>
<meta charset="utf-8">
<title>Pine Hollow Construction – Billboard</title>
<link rel="stylesheet" href="https://fonts.googleapis.com/css2?family=Oswald:wght@500;700&display=swap">
<style>
  :root {
    --ink: #000000;
    --signal-red: #ff0000;
    --paper: #ffffff;
    --stage: #e9ebee;
    --sky: #a9b8c8;
    --facade: #9fae9e;
    --roof: #5d6b6a;
  }
  html, body {
    margin: 0;
    padding: 0;
    width: 1200px;
    height: 1129px;
    overflow: hidden;
    background: var(--stage);
  }
  .billboard {
    position: absolute;
    left: 0;
    top: 326px;
    width: 1200px;
    height: 476px;
    display: block;
  }
  .headline {
    font-family: "Oswald", sans-serif;
    font-weight: 700;
    fill: var(--paper);
  }
  .phone-number {
    font-family: "Oswald", sans-serif;
    font-weight: 500;
    fill: var(--paper);
  }
  .brand-name {
    font-family: "Oswald", sans-serif;
    font-weight: 500;
    fill: var(--paper);
  }
  .services {
    font-family: "Oswald", sans-serif;
    font-weight: 500;
    fill: var(--signal-red);
    letter-spacing: 0.5px;
  }
  .panel-dark { fill: var(--ink); }
  .panel-red { fill: var(--signal-red); }
</style>
</head>
<body>
<svg class="billboard" viewBox="0 0 1200 476" xmlns="http://www.w3.org/2000/svg" aria-labelledby="bb-title">
  <title id="bb-title">Pine Hollow Construction billboard: Quality you deserve, service you can count on</title>
  <defs>
    <linearGradient id="house-tones" x1="0" y1="0" x2="0" y2="1">
      <stop offset="0" stop-color="var(--sky)"/>
      <stop offset="0.35" stop-color="var(--roof)"/>
      <stop offset="0.7" stop-color="var(--facade)"/>
      <stop offset="1" stop-color="#b9b7a6"/>
    </linearGradient>
  </defs>

  <rect class="panel-dark" x="0" y="0" width="1200" height="476"/>

  <!-- red chevron edge -->
  <polygon class="panel-red" points="496,0 526,0 632,184 534,353 502,353 604,184"/>

  <!-- house photo area -->
  <polygon role="img" aria-label="Photo of a two-storey house with a new grey shingle roof under a cloudy sky"
           fill="url(#house-tones)" points="0,0 496,0 604,184 502,353 0,353"/>

  <!-- red phone band -->
  <polygon class="panel-red" points="534,353 1200,353 1200,476 441,476"/>

  <!-- slogan -->
  <text class="headline" x="1162" y="157" text-anchor="end" font-size="158" textLength="480" lengthAdjust="spacingAndGlyphs">QUALITY</text>
  <text class="headline" x="1162" y="256" text-anchor="end" font-size="86" textLength="489" lengthAdjust="spacingAndGlyphs">YOU DESERVE,</text>
  <text class="headline" x="1162" y="315" text-anchor="end" font-size="44" textLength="496" lengthAdjust="spacingAndGlyphs">SERVICE YOU CAN COUNT ON</text>

  <!-- phone -->
  <g class="phone-icon" transform="translate(583 413)">
    <circle r="39" fill="var(--ink)"/>
    <path fill="var(--paper)" d="M-19,-17 C-21,-13 -21,-6 -16,3 C-10,13 -2,20 7,23 C12,24 15,22 17,19 L19,15 C20,13 19,11 17,10 L10,6 C8,5 6,6 5,7 L3,10 C-3,7 -8,1 -10,-5 L-7,-7 C-5,-8 -5,-10 -6,-12 L-10,-19 C-11,-21 -13,-22 -15,-21 Z"/>
    <path fill="none" stroke="var(--paper)" stroke-width="3.5" stroke-linecap="round" d="M2,-12 A10,10 0 0 1 11,-3"/>
    <path fill="none" stroke="var(--paper)" stroke-width="3.5" stroke-linecap="round" d="M3,-21 A19,19 0 0 1 20,-4"/>
  </g>
  <text class="phone-number" x="1155" y="449" text-anchor="end" font-size="98" textLength="495" lengthAdjust="spacingAndGlyphs">555-014-2876</text>

  <!-- brand and services -->
  <text class="brand-name" x="215" y="408" text-anchor="middle" font-size="38">Pine Hollow Construction</text>
  <text class="services" x="215" y="446" text-anchor="middle" font-size="20" textLength="390" lengthAdjust="spacingAndGlyphs">ROOF REPLACEMENT · GUTTERS · SIDING · SNOW REMOVAL</text>
</svg>
</body>
</html>
```